依頼概要
■ 依頼の目的/概要

鍼灸マッサージ治療院で手書きちらし制作 イラスト入りでの依頼
サンプル参考に
サイズ A4両面26.5cm×19cm
表面(アンチエイジング ダイエット 病状 健康法 食事 季節 等で心を軽く引き込む様な興味をそそるネタでなんとなく脳に興味をもたせるせ(イラストを使い視覚的に興味を持たせる)自分の隠れた欲求をきずかさせる内容に5~6にコマワリしてJPEGで貼り付けできる可能な様に)
紙面構成やコマワリはお任せします。タイトルやトピックなど記事やイラストで構成してください。 過去の紙面などあればプレゼンしてください。
裏面 (こちらから治療に関する原稿を出すので 手書きイラストで描いてください。1/3は治療院のメッセージボード用に空き)

現在、書いて頂きたいテーマは、主に女性に訴求する内容です。ヒントは以下のようなものになります。

(不妊治療、妊娠したい、不眠症・安眠、顎関節症、腰痛、坐骨神経痛、肩こり解消、アトピー、花粉症、わきが、多汗症、体臭、便秘解消、宿便、ほくろ除去、尿漏れ、他痛み)
病気(がん、高血圧、コレステロール、糖尿病、心筋梗塞、脳卒中、脳梗塞、青汁)
・スポーツ
(ゴルフ、テニス、野球、サッカー、筋トレ、柔軟ストレッチ、ダンス、釣り)
・美容
(美容商品レビュー、バストアップ、ニキビ、プラセンタ、肉割れ、妊娠線、セルライト、エステ選び、エステ体験、ソアリカ他、二重、豊胸、セルライト、エクステ、フェイシャル、リフレクソロジー、体臭、目のくま、美顔器、脱毛、白髪染め、洗顔、クレンジング他)
・ダイエット
(産後ダイエット、脂肪、足痩せ、顔痩せ、小顔)

食事
(話題の健康食レシピ 話題のサプリ 話題の食材など)

■応募資格
特にありませんが、見て興味を抱かせる内容のコンテンツを求めます

■ デザインへの要望

思わず鍼灸やマッサージを受けたくなるような、手書きイラスト入りで分かりやすいデザインをお願いします。
■ 納品ファイルの希望

高解像度JPG形式/

■ 利用用途

チラシのみ
記事とイメージです 参考にしてください

おつかれさまでした

また機会がありましたらよろしくお願いします。

```html
<!DOCTYPE html>
<html lang="ja">
<head>
<meta charset="utf-8">
<title>〇〇新聞</title>
<link rel="stylesheet" href="https://fonts.googleapis.com/css2?family=Klee+One:wght@400;600&family=Yomogi&display=swap">
<style>
:root{
  --ink:#1a1a1a;
  --paper:#ffffff;
  --tone:#e6e6e6;
}
*{margin:0;padding:0;box-sizing:border-box}
html,body{width:826px;height:1200px;overflow:hidden;background:var(--paper)}
.sheet{position:relative;width:826px;height:1200px;color:var(--ink);font-family:"Klee One",cursive}
.v{writing-mode:vertical-rl;position:absolute;line-height:1.55;letter-spacing:.04em}
.body{font-size:13px}
.masthead{position:absolute;left:688px;top:12px;width:118px;height:392px;border:2.5px solid var(--ink);border-radius:14px;display:flex;justify-content:center;align-items:center}
.masthead h1{writing-mode:vertical-rl;font-family:"Klee One",cursive;font-weight:600;font-size:74px;letter-spacing:.02em;line-height:1}
.greeting-title{left:600px;top:40px;font-size:22px;font-family:"Yomogi",cursive}
.headline{position:absolute;left:428px;top:12px;width:54px;height:312px;border:2px solid var(--ink);display:flex;justify-content:center;align-items:center}
.headline h2{writing-mode:vertical-rl;font-size:21px;font-weight:600;line-height:1.2;white-space:nowrap;letter-spacing:0}
.rule{position:absolute;border-top:2px dashed var(--ink)}
.badge{position:absolute;left:592px;top:345px;width:90px;height:255px;border:2px solid var(--ink);border-radius:50%;display:flex;justify-content:center;align-items:center}
.badge h3{writing-mode:vertical-rl;font-size:18px;font-weight:600;line-height:1.2;white-space:nowrap;letter-spacing:0}
.lead{left:784px;top:416px;font-size:12px;font-family:"Yomogi",cursive;white-space:nowrap;line-height:1.2}
.art{position:absolute;background:var(--tone);border-radius:10px}
.point{position:absolute;left:424px;top:752px;width:32px;height:90px;background:var(--ink);color:var(--paper);display:flex;justify-content:center;align-items:center}
.point span{writing-mode:vertical-rl;font-size:14px;font-weight:600}
.bubble{position:absolute;border:1.5px solid var(--ink);border-radius:50%}
</style>
</head>
<body>
<div class="sheet">

  <div class="masthead"><h1>〇〇新聞</h1></div>
  <p class="v greeting-title">ごあいさつ</p>

  <div class="headline"><h2>漢方はダイエットに効く？</h2></div>
  <p class="v body" style="left:150px;top:16px;height:300px;width:262px">
    最近は漢方薬も、人の体の「バランス」を整えることを考える医学です。体のめぐりを良くして余分なものを外に出すことで、自然に体重が落ちやすい体をつくります。ただし、すぐに効くものではありません。自分の体質に合ったものを選ぶことが大切です。そこで、まずは自分の肥満タイプを知ることから始めてみましょう。
  </p>
  <div class="art" role="img" aria-label="体重を気にする女性のイラスト" style="left:22px;top:180px;width:118px;height:140px"></div>

  <div class="rule" style="left:10px;top:336px;width:576px"></div>

  <div class="badge"><h3>漢方での肥満タイプ４☆</h3></div>
  <p class="v lead">まずは自分のタイプを知ろう!!</p>

  <p class="v body" style="left:692px;top:440px;height:560px;width:84px">
    ●脂肪太りタイプ　食べすぎや甘い物が多く、胃腸に熱がこもりがち。お腹まわりに脂肪がつき、汗をかきやすく便秘ぎみ。食事の量と時間を見直しましょう。
  </p>
  <div class="art" role="img" aria-label="食べすぎてお腹を押さえる女性のイラスト" style="left:700px;top:1010px;width:104px;height:175px"></div>

  <p class="v body" style="left:484px;top:348px;height:225px;width:100px">
    ●水太りタイプ　むくみやすく、体が冷えやすい。水分の代謝が悪く、下半身が重たい感じ。
  </p>
  <div class="art" role="img" aria-label="むくみに悩む女性のイラスト" style="left:480px;top:585px;width:110px;height:120px"></div>

  <p class="v body" style="left:600px;top:612px;height:390px;width:84px">
    ●気太りタイプ　ストレスでつい食べすぎてしまう。イライラしやすく、気のめぐりが滞りがち。
  </p>

  <p class="v body" style="left:385px;top:348px;height:390px;width:88px">
    ●血太りタイプ　血のめぐりが悪く、冷えや肩こりが出やすい。顔色がくすみがちです。
  </p>
  <div class="art" role="img" aria-label="肩こりに悩む女性のイラスト" style="left:300px;top:372px;width:80px;height:150px"></div>
  <div class="bubble" style="left:300px;top:540px;width:70px;height:50px"></div>
  <p class="v body" style="left:16px;top:348px;height:390px;width:272px">
    ●その他のタイプ　ひとつのタイプだけでなく、いくつかが重なっている方も多いもの。年齢や季節、生活習慣によっても体質は変わります。気になる症状があれば、一度ご相談ください。鍼灸やマッサージで、めぐりを整えることもできます。
  </p>

  <div class="rule" style="left:10px;top:745px;width:586px"></div>

  <div class="point"><span>ポイント</span></div>
  <p class="v body" style="left:16px;top:760px;height:230px;width:400px">
    漢方でダイエットをする場合、一番大切なのは自分の体質を知ること。体に合わないものを続けると、かえって体調を崩すことも。食事・睡眠・運動のバランスを整えながら、無理なく続けることが成功への近道です。
  </p>
  <div class="art" role="img" aria-label="笑顔の女性のイラスト" style="left:468px;top:950px;width:100px;height:105px"></div>
  <p class="v body" style="left:290px;top:1005px;height:180px;width:170px">
    自分のタイプを知ってどんな方法が合うのか、ぜひ試してみてください。
  </p>

</div>
</body>
</html>
```